TRVL-NINE Web Design

We are a Health, Safety, Environmental & Quality Recruitment Agency, our clients are major corporate Mining, Oil & Gas and Engineering companies. We have offices in Perth & Melbourne, Australia

The website should be very functional & easy to navigate

BUT REALLY LOOKING FOR WOW FACTOR!

Please Note: TRVL CORPORATE IS OUR OLD COMPANY THE NEW ONE IS "TRVL-NINE" 

Some idea's from our competitors:

http://www.guardlinepeak.com.au/
http://www.vantagehiring.com.au/
http://www.brightpick.com.au/
http://www.kovastaffing.co.uk/
http://www.jobmarrow.com/health-safety-environment-jobs

Would love to see some of our valued clients and there logos

still looking for wow factor

Industry/Entity Type

Mining

Requirements
Must have
• A place where candidates can upload there resumes & other contact details
• eg: http://www.guardlinepeak.com.au/candidates/register-your-resume/
• A place we can load jobs on to eg: http://www.guardlinepeak.com.au/vacancies/
• Contact details:
• Perth: 12 Kestrel Ave, West Perth, Western Australia 6005
• t: 08 7153 4406 | f: 08 7153 4470 |
• Melbourne: Level 1, 218 Arbour Lane, Melbourne, Victoria 3000
• t: 03 6214 5072| f: 03 6231 4095 |
• e: dennisk@trvlnine.com.au | w: http://www.trvlnine.com.au

```html
<!DOCTYPE html>
<html lang="en">
<head>
<meta charset="utf-8">
<title>TRVL-NINE | Health, Safety, Environment &amp; Quality Recruitment</title>
<link rel="stylesheet" href="https://fonts.googleapis.com/css2?family=Source+Sans+3:wght@400;600;700&display=swap">
<style>
:root{
  --blue:#1d8fd8;
  --blue-dark:#0f6eae;
  --navy:#1b3f6b;
  --navy-deep:#133256;
  --text:#3c3c3c;
  --red:#c0141b;
  --orange:#f7931e;
  --yellow:#f5e400;
  --footer:#1e1e1e;
  --footer-panel:#262626;
  --footer-bottom:#141414;
  --footer-text:#a8a8a8;
  --page:#ffffff;
}
*{box-sizing:border-box;margin:0;padding:0}
html,body{width:1200px;height:2247px;overflow:hidden;background:var(--page)}
body{font-family:"Source Sans 3",Arial,sans-serif;color:var(--text);position:relative}
.abs{position:absolute}

/* header */
.site-header{position:absolute;left:0;top:0;width:1200px;height:171px;
  background:radial-gradient(circle at 1000px 40px,#fff 0,#f4f4f4 40%,#e6e6e6 100%);border-top:2px solid #cfcfcf}
.bokeh{position:absolute;border-radius:50%;border:1px solid rgba(255,255,255,.9);background:rgba(255,255,255,.35)}
.brand{position:absolute;left:150px;top:40px;display:flex;align-items:center;gap:18px}
.brand-mark{width:96px;height:96px;background:var(--blue)}
.brand-name{font-size:58px;font-weight:400;color:var(--blue);letter-spacing:1px}
.account-btn{position:absolute;top:46px;height:32px;background:linear-gradient(#fafafa,#e4e4e4);border:1px solid #d4d4d4;
  font-size:13px;color:#333;display:flex;align-items:center;gap:8px;padding-left:14px}
.search-box{position:absolute;left:810px;top:112px;width:252px;height:29px;display:flex;border:1px solid #cfcfcf;background:#fff;border-radius:3px;overflow:hidden}
.search-box span{flex:1;font-size:12px;color:#999;display:flex;align-items:center;gap:10px;padding-left:10px}
.search-box b{width:40px;background:#3d7fd3;color:#fff;font-weight:400;font-size:12px;display:flex;align-items:center;justify-content:center}

/* nav */
.main-nav{position:absolute;left:0;top:171px;width:1200px;height:49px;background:linear-gradient(#4fc0f3,var(--blue) 55%,#1679bf)}
.main-nav a{position:absolute;top:14px;color:#fff;text-decoration:none;font-size:16px;font-weight:600}
.nav-sep{position:absolute;top:10px;width:1px;height:30px;background:rgba(255,255,255,.35)}

/* hero */
.hero{position:absolute;left:0;top:220px;width:1200px;height:585px;
  background:
    radial-gradient(ellipse 260px 120px at 830px 330px,rgba(230,190,110,.55),transparent 70%),
    radial-gradient(ellipse 300px 90px at 270px 380px,rgba(170,200,230,.35),transparent 70%),
    radial-gradient(ellipse 500px 70px at 650px 400px,rgba(240,170,50,.55),transparent 70%),
    linear-gradient(180deg,#16203a 0%,#243152 30%,#3d4a6e 48%,#5a5a62 58%,#7d6330 64%,#1a1814 68%,#23201a 76%,#4a3a1e 80%,#141414 88%,#0b0e14 100%)}
.hero-caption{position:absolute;left:0;top:505px;width:1200px;height:77px;background:rgba(110,110,110,.55)}
.hero-caption h2{position:absolute;left:260px;top:22px;font-size:26px;font-weight:400;color:#fff}
.hero-btn{position:absolute;left:744px;top:20px;width:144px;height:36px;border:1px solid #aaa;background:#3e3e3e;color:#fff;font-size:16px;display:flex;align-items:center;justify-content:center}
.hero-arrow{position:absolute;top:252px;width:30px;height:30px;border-radius:50%;background:#bdbdbd}

/* feature circles */
.feature{position:absolute;top:849px;width:228px;height:228px;border-radius:50%;overflow:hidden;border:4px solid #fff;box-shadow:0 0 0 1px #ddd,0 4px 8px rgba(0,0,0,.2)}
.feature-photo{position:absolute;inset:0}
.feature-label{position:absolute;left:0;bottom:0;width:100%;height:74px;background:var(--navy);text-align:center;color:#fff}
.feature-label strong{display:block;font-size:20px;font-weight:400;font-variant:small-caps;margin-top:8px}
.feature-label em{display:block;font-style:normal;color:var(--yellow);font-size:14px;font-weight:600}
.feature-shadow{position:absolute;left:200px;top:1112px;width:780px;height:20px;background:radial-gradient(ellipse at center,rgba(0,0,0,.18),transparent 70%)}

/* headings */
.section-title{position:absolute;font-size:26px;font-weight:400;font-variant:small-caps;color:#222}
.section-title span{color:var(--navy);font-weight:600}
.dotted{position:absolute;height:0;border-top:2px dotted #c9c9c9}

.welcome p{position:absolute;left:185px;width:560px;font-size:13px;line-height:18px;text-align:justify;color:var(--text)}
.btn-pill{position:absolute;font-size:13px;display:flex;align-items:center;justify-content:center;border-radius:3px}
.btn-blue{background:linear-gradient(#b9dcf5,#7fbde9);color:#1c3350;border:1px solid #7aaed6}
.btn-grey{background:#e0e0e0;color:#222}

/* job search */
.job-search{position:absolute;left:790px;top:1188px;width:247px;height:324px;background:linear-gradient(#1d4f80,var(--navy-deep));border-top:4px solid #2e6aa5;box-shadow:0 6px 8px rgba(0,0,0,.18)}
.job-search h3{position:absolute;left:22px;top:14px;font-size:20px;font-weight:400;font-variant:small-caps;color:#fff}
.select{position:absolute;left:18px;width:217px;height:27px;background:#fff;border-radius:2px;font-size:11.5px;color:#666;padding-left:14px;display:flex;align-items:center}
.select svg{position:absolute;right:12px;top:10px}
.submit{position:absolute;left:128px;top:271px;width:104px;height:28px;background:linear-gradient(#ffb43f,var(--orange));border-radius:4px;color:#fff;font-size:14px;font-weight:600;display:flex;align-items:center;justify-content:center}

/* latest jobs */
.job{position:absolute;left:205px;font-size:12.5px;line-height:18px;color:var(--text)}
.job .title{font-size:15px;color:#222}
.job .title::before{content:"›";position:absolute;left:-14px;color:#555}
.job .view{color:var(--red);font-weight:600}

.member-box{position:absolute;left:795px;top:1605px;width:218px;height:215px;border:1px solid #ddd}
.badge{position:absolute;left:40px;width:131px;height:88px}

/* footer */
.site-footer{position:absolute;left:0;top:1845px;width:1200px;height:305px;background:var(--footer)}
.panel{position:absolute;top:31px;height:241px;background:var(--footer-panel);border:1px solid #3a3a3a}
.office{position:absolute;top:28px;font-size:12px;line-height:17px;color:var(--footer-text)}
.office h4{font-size:15px;font-weight:400;color:#cfcfcf;margin-bottom:9px}
.office .gap{height:23px}
.testimonials h4{position:absolute;left:22px;top:14px;font-size:17px;font-weight:400;color:#e5e5e5}
.avatar{position:absolute;left:10px;width:54px;height:54px;border-radius:50%}
.quote{position:absolute;left:72px;width:165px;font-size:11px;line-height:15px;color:var(--footer-text);text-align:justify}
.more{position:absolute;right:14px;top:212px;font-size:11px;color:#f2b705}
.footer-bottom{position:absolute;left:0;top:2150px;width:1200px;height:97px;background:var(--footer-bottom);border-top:1px solid #2c2c2c}
.social{position:absolute;top:30px;width:18px;height:18px;border-radius:2px}
.legal{position:absolute;right:170px;top:24px;font-size:11px;color:#d0d0d0;text-align:right;line-height:23px}
</style>
</head>
<body>

<header class="site-header">
  <div class="bokeh" style="left:610px;top:-40px;width:120px;height:120px"></div>
  <div class="bokeh" style="left:700px;top:20px;width:90px;height:90px"></div>
  <div class="bokeh" style="left:1060px;top:-30px;width:140px;height:140px"></div>
  <div class="bokeh" style="left:1140px;top:60px;width:80px;height:80px"></div>
  <div class="brand">
    <div class="brand-mark"></div>
    <div class="brand-name">TRVL-NINE</div>
  </div>
  <div class="account-btn" style="left:840px;width:95px">
    <svg width="12" height="14" viewBox="0 0 12 14"><rect x="1" y="6" width="10" height="8" fill="#333"/><path d="M3 6V4a3 3 0 0 1 6 0v2" stroke="#333" stroke-width="2" fill="none"/></svg>Login</div>
  <div class="account-btn" style="left:942px;width:120px">
    <svg width="12" height="14" viewBox="0 0 12 14"><rect x="1" y="1" width="10" height="13" fill="#333"/><rect x="3" y="4" width="6" height="1.5" fill="#ddd"/><rect x="3" y="7" width="6" height="1.5" fill="#ddd"/></svg>Register</div>
  <div class="search-box"><span><svg width="12" height="12" viewBox="0 0 12 12"><circle cx="5" cy="5" r="3.8" stroke="#888" stroke-width="1.6" fill="none"/><path d="M8 8l3 3" stroke="#888" stroke-width="1.8"/></svg>Search</span><b>GO</b></div>
</header>

<nav class="main-nav">
  <a style="left:175px">Home</a><i class="nav-sep" style="left:244px"></i>
  <a style="left:274px">About Us</a><i class="nav-sep" style="left:364px"></i>
  <a style="left:394px">For Candidates</a><i class="nav-sep" style="left:523px"></i>
  <a style="left:553px">For Employers</a><i class="nav-sep" style="left:678px"></i>
  <a style="left:708px">Sectors</a><i class="nav-sep" style="left:785px"></i>
  <a style="left:815px">Search</a><i class="nav-sep" style="left:888px"></i>
  <a style="left:918px">Contact Us</a>
</nav>

<section class="hero" role="img" aria-label="Night view of an industrial power plant with cooling tower and cranes, lights reflected in the river">
  <div class="hero-arrow" style="left:30px"><svg width="30" height="30" viewBox="0 0 30 30"><path d="M17 9l-6 6 6 6" stroke="#555" stroke-width="3" fill="none"/></svg></div>
  <div class="hero-arrow" style="left:1122px"><svg width="30" height="30" viewBox="0 0 30 30"><path d="M13 9l6 6-6 6" stroke="#555" stroke-width="3" fill="none"/></svg></div>
  <div class="hero-caption">
    <h2>Focusing on the Resources Industry</h2>
    <div class="hero-btn">Learn More</div>
  </div>
</section>

<div class="feature" style="left:178px">
  <div class="feature-photo" role="img" aria-label="Group of business professionals" style="background:linear-gradient(170deg,#f4f4f4 0%,#e2d6cc 35%,#6a6660 55%,#2a2a2e 75%)"></div>
  <div class="feature-label"><strong>Employer</strong><em>Clickhere &gt;&gt;</em></div>
</div>
<div class="feature" style="left:463px">
  <div class="feature-photo" role="img" aria-label="Business handshake" style="background:linear-gradient(135deg,#fbfbfb 0%,#e9e9e9 35%,#d9a98a 55%,#3a3f4a 80%)"></div>
  <div class="feature-label"><strong>Candidates</strong><em>Register Here &gt;&gt;</em></div>
</div>
<div class="feature" style="left:753px">
  <div class="feature-photo" role="img" aria-label="Offshore oil platform" style="background:linear-gradient(#e4e8ec 0%,#8c939a 30%,#4a4f55 50%,#e0c21a 60%,#c9a915 68%)"></div>
  <div class="feature-label"><strong>Vacancies</strong><em>Clickhere &gt;&gt;</em></div>
</div>
<div class="feature-shadow"></div>

<section class="welcome">
  <h2 class="section-title" style="left:181px;top:1170px">Welcome to <span>TRVLCORP</span></h2>
  <div class="dotted" style="left:181px;top:1212px;width:434px"></div>
  <p style="top:1233px">An independent specialised Health, Safety, Environment and Quality Recruitment Company was a vision of our company founder for many years in early 2008 that vision became a reality with the birth of trvl nine. We are Australian privately owned and operated recruitment service company with offices in Perth Western Australia.</p>
  <p style="top:1341px">We operate exclusively in the Mining, Oil and Gas, Construction and Engineering sectors and our clients range from engineering consultancies, major owner operator oil companies, international EPCM's to the largest diversified mining companies in the world.</p>
  <p style="top:1413px">Inclusive to providing Health Safety, Environment and Quality professionals of all levels we also provide Risk Management, Emergency Response and Training personal. These professionals are sourced locally and internationally to meet the unique requirements of our clients and candidates alike in today's dynamic and ever changing work place.</p>
  <div class="btn-pill btn-blue" style="left:652px;top:1483px;width:92px;height:38px">learn more</div>
</section>

<aside class="job-search">
  <h3>Job Search</h3>
  <div class="select" style="top:59px">Category<svg width="8" height="6" viewBox="0 0 8 6"><path d="M1 1l3 3 3-3" stroke="#555" stroke-width="1.5" fill="none"/></svg></div>
  <div class="select" style="top:99px">Sub Category<svg width="8" height="6" viewBox="0 0 8 6"><path d="M1 1l3 3 3-3" stroke="#555" stroke-width="1.5" fill="none"/></svg></div>
  <div class="select" style="top:141px">Work Type<svg width="8" height="6" viewBox="0 0 8 6"><path d="M1 1l3 3 3-3" stroke="#555" stroke-width="1.5" fill="none"/></svg></div>
  <div class="select" style="top:181px">Location<svg width="8" height="6" viewBox="0 0 8 6"><path d="M1 1l3 3 3-3" stroke="#555" stroke-width="1.5" fill="none"/></svg></div>
  <div class="select" style="top:222px">Area<svg width="8" height="6" viewBox="0 0 8 6"><path d="M1 1l3 3 3-3" stroke="#555" stroke-width="1.5" fill="none"/></svg></div>
  <div class="submit">Submit</div>
</aside>

<section class="latest-jobs">
  <h2 class="section-title" style="left:181px;top:1552px">Latest Jobs</h2>
  <div class="dotted" style="left:181px;top:1590px;width:306px"></div>
  <div class="job" style="top:1607px"><div class="title">Casual Safety Advisors Shop&nbsp; Refurbishment</div>Permanent Full Time<br>Sydney<br><span class="view">View »</span></div>
  <div class="job" style="top:1688px"><div class="title">Occupational Health Nurse Heavy Industry</div>Contract or Temp<br>Sydney<br><span class="view">View »</span></div>
  <div class="btn-pill btn-grey" style="left:191px;top:1778px;width:91px;height:37px">Learn More</div>
</section>

<section class="sectors">
  <h2 class="section-title" style="left:530px;top:1552px">Sectors</h2>
  <div class="dotted" style="left:530px;top:1590px;width:222px"></div>
  <div class="abs" role="img" aria-label="Offshore supply vessel at sea" style="left:535px;top:1607px;width:215px;height:91px;border:1px solid #ccc;background:linear-gradient(#d5dde3 0%,#a9b6c0 35%,#f0f0f0 48%,#e8451f 58%,#d63a1a 72%,#3d5d7a 82%,#2b4660 100%)"></div>
  <p class="abs" style="left:535px;top:1705px;width:210px;font-size:12.5px;line-height:18px;text-align:justify">At TRVL Corp we specialise in the Mining, Oil, Gas, Engineering and Construction industry sectors.</p>
  <div class="btn-pill btn-grey" style="left:540px;top:1778px;width:92px;height:37px">Learn More</div>
</section>

<section class="members">
  <h2 class="section-title" style="left:791px;top:1552px">Member</h2>
  <div class="dotted" style="left:791px;top:1590px;width:222px"></div>
  <div class="member-box">
    <div class="badge" style="top:11px;background:#ffffff;border:1px solid #d6d6d6"></div>
    <div class="badge" style="top:102px;height:101px;background:#5b2a8c"></div>
  </div>
</section>

<footer class="site-footer">
  <div class="panel" style="left:162px;width:573px">
    <div class="office" style="left:24px">
      <h4>Perth Office</h4>
      Suite 7, 306 Halden Road<br>Wembury<br>&nbsp;Western Australia 6008
      <div class="gap"></div>
      P | +61 (0) 8 5120 7734<br>P | +61 (0) 8 5120 7734<br>E | info@trvlcorp.com.au
    </div>
    <div class="office" style="left:201px">
      <h4>Brisbane Office</h4>
      Level 21, Harbour Plaza One<br>112 Quill Street, Brisbane<br>Queensland 4000
      <div class="gap"></div>
      P | +61 (0) 7 5820 3391<br>F | +61 (0) 7 5820 3392<br>E | info@trvlcorp.com.au
    </div>
    <div class="office" style="left:386px">
      <h4>Seoul Office</h4>
      Level 33, Lumen Trade Tower<br>208 Hanbit-ro<br>Dawon-dong<br>Seoul, Republic of Korea
      <div class="gap" style="height:6px"></div>
      P | +82 (0) 2 4180 5521<br>F | +82 (0) 2 4180 5522<br>E | minjuk@trvlcorp.com.au
    </div>
  </div>
  <div class="panel testimonials" style="left:773px;width:249px">
    <h4>Testimonials</h4>
    <div class="avatar" role="img" aria-label="Client portrait" style="top:58px;background:#8a6b55"></div>
    <p class="quote" style="top:58px">Sed ut perspiciatis unde omnis iste natus error sit voluptatem accusantium doloremque rem</p>
    <div class="avatar" role="img" aria-label="Client portrait" style="top:135px;background:#4a3c38"></div>
    <p class="quote" style="top:136px">Sed ut perspiciatis unde omnis iste natus error sit voluptatem accusantium doloremque rem</p>
    <span class="more">More &gt;&gt;</span>
  </div>
</footer>

<div class="footer-bottom">
  <span class="social" style="left:162px;background:#3b5a9a"></span>
  <span class="social" style="left:186px;background:#2ba6de"></span>
  <span class="social" style="left:210px;background:#5d5d5d"></span>
  <span class="social" style="left:234px;background:#f39325"></span>
  <span class="social" style="left:258px;background:#d0362b"></span>
  <span class="social" style="left:282px;background:#6b9fc4"></span>
  <div class="legal">Home | Rss Feed | Login | Register | Privacy policy | Legal | Testimonials<br>© 2013&nbsp; trvlcorp.com. All Rights Reserved.</div>
</div>

</body>
</html>
```